brindle's business card for earthmoving and tipper hire business.

I have a small earthmoving and tipper truck company. I am aiming for the smaller jobs that the big guys don't want. I am also Doing grass slashing and fire hazard reduction work. I would like to see some earthy colors, greens browns etc. I have a tractor with a front end loader attachment, and a 22 ton tipper. I would like to maybe have a silhouette of a tipper and tractor/slasher/loader setup in centre with my business name over the top and details to one side or something like that

Industry/Entity Type

Business

Contact Information for Business Card

Brindle's small earthworks and tipper hireToowoombaABN: 47781050480PH 0479126773Email brindle.4@fenwickmail.com

Font styles to use
Sans Serif

Colors
fbee3d
abd036
85cae6
f78f20

Requirements
Nice to have
• Earthy colors . business name in blue

```html
<!DOCTYPE html>
<html lang="en">
<head>
<meta charset="utf-8">
<title>Brindle's business card</title>
<link rel="stylesheet" href="https://fonts.googleapis.com/css2?family=Cabin:wght@600;700&family=Josefin+Sans:wght@300;400;600&family=Open+Sans:wght@400;700&display=swap">
<style>
  :root {
    --backdrop: #e6a892;
    --earth-brown: #3a2620;
    --earth-brown-deep: #2e1e19;
    --field-green: #3f8b5a;
    --panel-green: #4e8c5f;
    --silhouette-green: #2f6b45;
    --sky-blue: #a9d6ea;
    --cream: #f1ead8;
    --white: #ffffff;
  }
  * { box-sizing: border-box; margin: 0; padding: 0; }
  html, body { width: 1200px; height: 783px; overflow: hidden; }
  body {
    background: var(--backdrop);
    font-family: "Open Sans", sans-serif;
    position: relative;
  }
  .card {
    position: absolute;
    top: 243px;
    width: 520px;
    height: 297px;
    overflow: hidden;
    box-shadow: 0 8px 24px rgba(60, 30, 20, 0.25);
  }
  .card--front { left: 60px; }
  .card--back { left: 620px; }
  .card__ground { position: absolute; inset: 0; width: 100%; height: 100%; }

  /* front */
  .front__vehicle {
    position: absolute; left: 34px; top: 92px; width: 96px; height: 48px;
    background: var(--silhouette-green); border-radius: 4px;
  }
  .front__name {
    position: absolute; left: 210px; top: 128px;
    font-family: "Cabin", sans-serif; font-weight: 700; font-size: 58px;
    color: var(--sky-blue); letter-spacing: 1px; line-height: 1;
  }
  .front__tagline {
    position: absolute; left: 214px; top: 192px;
    font-family: "Josefin Sans", sans-serif; font-weight: 400; font-size: 17px;
    font-variant: small-caps; letter-spacing: 2px; color: var(--cream);
  }

  /* back */
  .back__tagline {
    position: absolute; left: 0; right: 0; top: 16px; text-align: center;
    font-family: "Josefin Sans", sans-serif; font-size: 14px;
    font-variant: small-caps; letter-spacing: 2px; color: var(--cream);
  }
  .back__name {
    position: absolute; left: 0; right: 0; top: 34px; text-align: center;
    font-family: "Cabin", sans-serif; font-weight: 700; font-size: 22px;
    color: var(--white); letter-spacing: 1px;
  }
  .back__vehicles {
    position: absolute; left: 200px; top: 66px; width: 120px; height: 42px;
    background: rgba(255, 255, 255, 0.75); border-radius: 4px;
  }
  .back__vehicle-faint {
    position: absolute; left: 26px; top: 200px; width: 80px; height: 40px;
    background: var(--silhouette-green); border-radius: 4px;
  }
  .panel {
    position: absolute; background: var(--panel-green); color: var(--white);
    border: 1px solid rgba(255, 255, 255, 0.15);
  }
  .panel--contact { left: 118px; top: 176px; width: 196px; height: 106px; padding: 10px 12px; }
  .panel--services { left: 324px; top: 126px; width: 180px; height: 104px; padding: 12px 14px; }
  .contact__name {
    text-align: center; font-family: "Cabin", sans-serif; font-weight: 700; font-size: 12px;
    letter-spacing: 1px;
  }
  .contact__detail {
    text-align: center; font-family: "Josefin Sans", sans-serif; font-size: 8px;
    line-height: 1.2; letter-spacing: 0.5px;
  }
  .contact__phone { margin-top: 10px; font-weight: 700; font-size: 13px; letter-spacing: 0.5px; }
  .contact__email { font-weight: 700; font-size: 10px; }
  .services { list-style: none; }
  .services li {
    display: flex; align-items: center; gap: 7px;
    font-family: "Josefin Sans", sans-serif; font-weight: 300; font-size: 13px;
    line-height: 20px;
  }
  .services__mark {
    width: 10px; height: 10px; border: 1px solid var(--white); border-radius: 50%; flex: none;
  }
</style>
</head>
<body>
  <section class="card card--front" aria-label="Business card front">
    <svg class="card__ground" viewBox="0 0 520 297" aria-hidden="true">
      <rect width="520" height="297" fill="var(--earth-brown)"/>
      <path d="M0,70 Q150,20 300,0 L520,0 L520,52 Q260,90 0,172 Z" fill="var(--field-green)"/>
    </svg>
    <div class="front__vehicle" role="img" aria-label="Tipper truck silhouette"></div>
    <h1 class="front__name">Brindle's</h1>
    <p class="front__tagline">Earthworks and tipper hire</p>
  </section>

  <section class="card card--back" aria-label="Business card back">
    <svg class="card__ground" viewBox="0 0 520 297" aria-hidden="true">
      <rect width="520" height="297" fill="var(--earth-brown)"/>
      <path d="M0,170 Q250,110 520,70 L520,0 L320,0 Q300,20 0,110 Z" fill="var(--field-green)"/>
      <path d="M0,170 Q250,110 520,70 L520,120 Q250,150 0,260 Z" fill="var(--earth-brown-deep)" opacity="0"/>
      <path d="M0,0 L320,0 Q160,50 0,90 Z" fill="var(--earth-brown)"/>
      <path d="M0,200 Q60,175 110,170 L110,297 L0,297 Z" fill="var(--field-green)"/>
    </svg>
    <p class="back__tagline">Earthworks and tipper hire</p>
    <h2 class="back__name">Brindle's</h2>
    <div class="back__vehicles" role="img" aria-label="Tractor with loader and tipper truck silhouettes"></div>
    <div class="back__vehicle-faint" role="img" aria-label="Faint tipper truck silhouette"></div>

    <div class="panel panel--contact">
      <p class="contact__name">Brindle's</p>
      <p class="contact__detail">small earthworks and tipper hire</p>
      <p class="contact__detail">KELBARRA</p>
      <p class="contact__detail">ABN 62194038715</p>
      <p class="contact__phone">Phone: 0438571629</p>
      <p class="contact__email">Email brindle.4@fenwickmail.com</p>
    </div>

    <div class="panel panel--services">
      <ul class="services">
        <li><span class="services__mark"></span>Earthmoving</li>
        <li><span class="services__mark"></span>Tipper hire</li>
        <li><span class="services__mark"></span>Grass slashing</li>
        <li><span class="services__mark"></span>Fire hazard reduction</li>
      </ul>
    </div>
  </section>
</body>
</html>
```